Etiketten für Honig
Zielgruppe
Es scheint Missverständnisse zu geben weshalb ich das Briefing wohl ändern muss.
see below for English translation
Wir sind eine kleine Imkerei, die von der Liebhaberei in den Nebenerwerb wechselt. Wir verkaufen verschiedene Sortenhonige und Honigzubereitungen (siehe Webseite) im vorwiegend ländlichen Raum des Münsterlandes.
Entsprechend unseres Standortes und unserer Kundschaft benötigen wir ein klassisch ländliches Design. Hierfür haben wir auch bereits ein Logo welches verwendet werden muss.
English
There seems to be some misunderstanding, so I guess I'll have to change the briefing.
We are a small apiary that changes from hobby to sideline. We sell different types of honey and honey preparations (e.g. honey with raspberry) in a predominantly rural area of the Münsterland (Muensterland).
According to our location and our clientele, we need a classic rural design. We already have a logo which must be used.
Aufgabenstellung
Wir möchten ein rechteckiges Etikett mit Gewährverschluss das für verschiedene Sorten adoptierbar ist. Zum Beispiel durch den Austausch der Sortenbezeichnung und eine farbliche Veränderung.
Das Design soll später auf Naturpapier oder Graspapier gedruckt werden. Das Logo muss auf Etikett und Gewährverschluss abgebildet werden.
We would like a rectangular label with a guarantee seal that is adoptable for different varieties. For example, by exchanging the variety designation and changing the color.
The design will later be printed on uncoated paper or grass paper. The logo must be shown on the label and guarantee seal.

```html
<!DOCTYPE html>
<html lang="de">
<head>
<meta charset="utf-8">
<title>Honigmanufaktur Wendholt – Etikett mit Gewährverschluss</title>
<link href="https://fonts.googleapis.com/css2?family=PT+Sans+Narrow:wght@400;700&family=Kaushan+Script&display=swap" rel="stylesheet">
<style>
  :root{
    --bg-light:#f7f7f7;
    --bg-dark:#c9c9c9;
    --paper:#ffffff;
    --leaf-green:#9acd00;
    --seal-text:#1f2a05;
    --ink:#4a4a4a;
    --ink-soft:#555555;
    --strip:#dcdcdc;
    --honey:#f5b800;
    --honey-deep:#f29a1f;
    --comb-light:#ffc24a;
  }
  *{margin:0;padding:0;box-sizing:border-box}
  html,body{width:1200px;height:1017px;overflow:hidden}
  body{
    background:radial-gradient(ellipse at 30% 40%,var(--bg-light) 0%,#e4e4e4 55%,var(--bg-dark) 100%);
    font-family:"PT Sans Narrow",sans-serif;
    position:relative;
  }
  .seal{position:absolute;left:0;top:0;width:1200px;height:640px}
  .seal-text{position:absolute;left:473px;width:258px;text-align:center;font-size:15px;line-height:1.2}
  .seal-brand{top:126px;font-weight:700;color:#7a5a00;font-size:17px}
  .seal-bbd{top:184px;color:var(--seal-text)}
  .seal-date{position:absolute;left:497px;top:204px;width:211px;height:37px;border-radius:19px;background:var(--paper)}
  .seal-region{top:250px;color:var(--seal-text)}
  .seal-storage{top:274px;color:var(--paper);font-weight:700;font-size:16px;line-height:21px}
  .stem-strip{position:absolute;left:589px;top:324px;width:27px;height:235px;background:var(--strip)}
  .weight{position:absolute;left:530px;width:145px;text-align:center;color:var(--ink)}
  .weight-value{top:566px;font-size:25px;font-weight:700}
  .weight-note{top:596px;font-size:18px}

  .label{
    position:absolute;left:117px;top:621px;width:971px;height:313px;
    background:var(--paper);border-radius:32px;overflow:hidden;
    box-shadow:0 2px 5px rgba(0,0,0,.18);
  }
  .variety-badge{
    position:absolute;left:42px;top:41px;width:152px;height:152px;border-radius:50%;
    border:4px solid var(--honey);background:var(--paper);
    display:flex;align-items:center;justify-content:center;z-index:2;
  }
  .variety-badge-inner{
    width:128px;height:128px;border-radius:50%;background:var(--honey);
    display:flex;flex-direction:column;align-items:center;justify-content:center;
    color:var(--paper);font-family:"Kaushan Script",cursive;font-size:26px;line-height:.95;
    transform:rotate(-18deg);
  }
  .brand-mark{position:absolute;left:425px;top:18px;width:120px;height:120px;border-radius:50%;border:4px solid var(--leaf-green)}
  .brand-name{
    position:absolute;left:285px;top:150px;width:400px;text-align:center;
    font-size:38px;color:var(--ink-soft);font-weight:400;letter-spacing:.5px;z-index:2;
  }
  .label-copy{
    position:absolute;right:49px;top:49px;width:135px;text-align:right;
    font-size:15px;line-height:20.3px;color:var(--ink);z-index:2;
  }
  .decor{position:absolute;z-index:1}
  .decor-left{left:0;top:196px;width:268px;height:117px;
    background:linear-gradient(120deg,#5aa42a 0%,var(--honey-deep) 40%,var(--comb-light) 70%,var(--honey-deep) 100%)}
  .decor-band{left:268px;top:275px;width:420px;height:38px;
    background:linear-gradient(180deg,var(--comb-light),var(--honey-deep))}
  .decor-right{left:688px;top:160px;width:283px;height:153px;
    clip-path:polygon(0 55px,240px 55px,240px 0,100% 0,100% 100%,0 100%);
    background:linear-gradient(200deg,var(--honey-deep) 0%,#fbd24a 45%,var(--comb-light) 70%,#f7a81f 100%)}
</style>
</head>
<body>
  <svg class="seal" viewBox="0 0 1200 640" aria-hidden="true">
    <defs>
      <filter id="soft" x="-10%" y="-10%" width="120%" height="120%">
        <feDropShadow dx="0" dy="1" stdDeviation="2" flood-opacity=".18"/>
      </filter>
    </defs>
    <g filter="url(#soft)">
      <rect x="530" y="300" width="145" height="330" fill="#ffffff"/>
      <polygon points="535,92 670,92 739,210 670,328 535,328 466,210" fill="#ffffff" stroke="#ffffff" stroke-width="12" stroke-linejoin="round"/>
    </g>
    <polygon points="541,104 664,104 726,210 664,318 541,318 479,210" fill="#9acd00" stroke="#9acd00" stroke-width="12" stroke-linejoin="round"/>
  </svg>

  <div class="seal-text seal-brand">Wendholt</div>
  <div class="seal-text seal-bbd">Mindestens haltbar bis</div>
  <div class="seal-date"></div>
  <div class="seal-text seal-region">Honig aus der Region</div>
  <div class="seal-text seal-storage">Kuhl, trocken und<br>dunkel lagern</div>
  <div class="stem-strip"></div>
  <div class="weight weight-value">500g</div>
  <div class="weight weight-note">mehrweglass</div>

  <div class="label">
    <div class="variety-badge">
      <div class="variety-badge-inner"><span>Honing</span><span>Type</span></div>
    </div>
    <div class="brand-mark"></div>
    <div class="brand-name">Honigmanufaktur Wendholt</div>
    <p class="label-copy">Lorem ipsum dolor sit amet, consectetur adipiscing elit, sed do eiusmod tempor incididunt ut labore et dolore magna aliqua.</p>
    <div class="decor decor-left" role="img" aria-label="Illustration: Honigwaben mit Kamillenblüte und grünen Blättern"></div>
    <div class="decor decor-band" role="img" aria-label="Illustration: Reihe orangefarbener Honigwaben"></div>
    <div class="decor decor-right" role="img" aria-label="Illustration: Wabenstücke mit Honig, Kamillenblüten, Blättern und einer Biene"></div>
  </div>
</body>
</html>
```